Website design for a Recruitment Agency in the Pacific Islands

Website for jobseekers to search for work, employers to list vacancies and also for workers to upload their resumes for possible job prospects.

The website will be called ' Korowai Staffing' and this needs to reflect the Pacific Islanders searching for jobs or working in the fields.
Must be connected to a database that collects details for workers which can be downloaded onto an excel spreadsheet for quick reviews offline
The website must also have an app for ios and android so this can be easily downloaded for individuals who want to do quick job searches without going onto the website.

The main objective of this website is to list job opportunities in all Pacific Island Countries or even overseas which Pacific Islanders can apply.

The theme of fishing means ' there is alot of fish in the sea ' = lots of workers in the Pacific Ocean.

Target Market(s)

Agriculture, Fisheries, constructions and mining

Industry/Entity Type

Agriculture, Constructions and Fisheries

Font styles to use
Other font styles liked:
• Muli

Colors
E54698
E96AAD
F1A4CE
F9D9EA
FCEFF6

Requirements
Must have
• Must have an App, adroid and ios
Nice to have
• - pictures of Pacific Islanders , pictures of Pacific Islanders at work in mines, in fisheries and in agricultures

```html
<!DOCTYPE html>
<html lang="en">
<head>
<meta charset="utf-8">
<title>Korowai Staffing — Find the right job for you</title>
<link rel="stylesheet" href="https://fonts.googleapis.com/css2?family=Lexend:wght@400;500&family=Mulish:wght@400;600;700&display=swap">
<style>
:root{
  --pink:#e6007e;
  --pink-hero:#e2007c;
  --plum:#9e0058;
  --plum-deep:#8a0050;
  --rose:#e96aad;
  --blush:#fcebf3;
  --ink:#1c1c1c;
  --grey-btn:#6b6b6b;
  --panel:#f4f4f4;
  --footer:#2b2b2b;
  --green:#19c431;
  --gold:#c29a13;
  --teal:#119fc0;
  --head:'Lexend',sans-serif;
  --body:'Mulish',sans-serif;
}
*{box-sizing:border-box;margin:0;padding:0}
html,body{width:1200px;height:3750px;overflow:hidden}
body{position:relative;font-family:var(--body);color:var(--ink);background:#fff}
a{color:inherit;text-decoration:none}

/* hero */
.hero{position:absolute;left:0;top:0;width:1200px;height:808px;background:linear-gradient(100deg,var(--pink-hero) 0%,#d80078 55%,var(--plum) 100%);overflow:hidden}
.hero-arc{position:absolute;left:0;top:0}
.nav{position:absolute;top:33px;right:293px;display:flex;gap:15px;font-size:13px;color:#fff;font-family:var(--body);white-space:nowrap}
.post-job{position:absolute;left:922px;top:20px;width:105px;height:41px;background:#fff;color:var(--pink);border-radius:4px;font:500 13.5px var(--head);display:flex;align-items:center;justify-content:center;letter-spacing:.4px}
.hero-mark{position:absolute;left:167px;top:15px;width:270px;height:342px;border-radius:50% 40% 45% 50%;background:radial-gradient(circle at 55% 50%,rgba(255,255,255,.22),rgba(255,255,255,0) 70%)}
.hero-word{position:absolute;left:713px;top:160px;font:500 118px var(--head);color:rgba(120,20,70,.45);letter-spacing:2px}
.hero-person{position:absolute;left:713px;top:167px;width:487px;height:641px;border-radius:240px 240px 0 0;background:linear-gradient(180deg,#c9a994 0%,#9c7d6d 45%,#7d6a66 100%)}
.brand{position:absolute;left:170px;top:408px;font:500 48px var(--head);color:#fff;letter-spacing:.5px;white-space:nowrap}
.tagline{position:absolute;left:171px;top:490px;font:600 22px var(--body);color:#fff}
.search{position:absolute;left:170px;top:543px;width:503px;height:64px;background:#fff;border:4px solid #f39ac8;border-radius:32px;display:flex;align-items:center;font-size:14px;color:#333}
.search .field{padding:0 16px;height:30px;display:flex;align-items:center;justify-content:space-between;border-right:1px solid #999;white-space:nowrap}
.search .field:last-of-type{border-right:none}
.caret{width:0;height:0;border-left:4px solid transparent;border-right:4px solid transparent;border-top:6px solid #333}
.search .go{margin-left:auto;margin-right:6px;width:96px;height:46px;border-radius:23px;background:var(--pink);color:#fff;font:500 14px var(--head);display:flex;align-items:center;justify-content:center}
.search-note{position:absolute;left:171px;top:624px;font:600 14px var(--body);color:#fff}

/* section headings */
.sec-title{position:absolute;left:0;width:1200px;text-align:center}
.sec-title .ghost{position:absolute;left:0;width:100%;text-align:center;font:500 64px var(--head);color:#fde6f0;top:-30px;letter-spacing:1px;line-height:1}
.sec-title h2{position:relative;font:500 28px var(--head);letter-spacing:.5px}

/* steps */
.step{position:absolute;top:986px;width:277px;height:145px;background:#fff;border-radius:26px;box-shadow:0 0 0 3px #f2f2f2,0 4px 10px rgba(0,0,0,.08);display:flex;align-items:center;padding:0 8px}
.step .ico{flex:none;width:116px;height:129px;border-radius:22px;display:flex;align-items:center;justify-content:center}
.step .txt{padding-left:10px}
.step h3{font:500 16px/22px var(--head)}
.step p{font-size:10.5px;line-height:16px;margin-top:6px;text-align:justify}

/* jobs */
.jobs-bg{position:absolute;left:0;top:1223px;width:1200px;height:898px;background:var(--blush)}
.job{position:absolute;left:170px;width:858px;height:189px;background:#fff;border-radius:30px;box-shadow:0 0 0 3px #fff,0 3px 12px rgba(0,0,0,.12)}
.job .logo{position:absolute;left:12px;top:10px;width:180px;height:169px;border:2px solid #e6e6e6;border-radius:26px;display:flex;align-items:center;justify-content:center;gap:8px;font:600 17px var(--body);color:#2a2a2a}
.job .logo i{display:block;width:14px;height:14px;border-radius:50%;background:var(--rose)}
.job h3{position:absolute;left:216px;top:36px;font:500 17px var(--head)}
.job .addr{position:absolute;left:216px;top:70px;font-size:13.5px}
.job .pay{position:absolute;left:220px;top:105px;width:140px;height:44px;border:2px solid #555;border-radius:6px;display:flex;align-items:center;justify-content:center;font:600 15px var(--body)}
.job .tag{position:absolute;right:30px;top:46px;height:38px;padding:0 10px;border-radius:4px;color:#fff;font:600 15px var(--body);display:flex;align-items:center}
.job .browse{position:absolute;right:30px;top:110px;font:500 17px var(--head);text-decoration:underline;text-underline-offset:4px}
.btn{position:absolute;display:flex;align-items:center;justify-content:center;border-radius:4px;color:#fff;background:var(--pink);font:600 15px var(--body)}

/* resume */
.resume-person{position:absolute;left:146px;top:2177px;width:342px;height:495px;border-radius:170px 170px 60px 60px;background:linear-gradient(180deg,#e9d7cc 0%,#d8d3cf 40%,#7b8fa8 100%)}
.resume-panel{position:absolute;left:459px;top:2194px;width:569px;height:449px;background:var(--panel);border-radius:40px;box-shadow:0 0 0 3px #fff,0 3px 12px rgba(0,0,0,.12)}
.resume-panel .kicker{position:absolute;left:41px;top:70px;font:500 18px var(--head)}
.resume-panel h2{position:absolute;left:41px;top:112px;font:500 28px/40px var(--head);letter-spacing:.3px}
.resume-panel p{position:absolute;left:42px;top:250px;width:500px;font-size:12.5px;line-height:22px}

/* articles */
.articles-bg{position:absolute;left:0;top:2730px;width:1200px;height:644px;background:var(--blush)}
.article{position:absolute;top:2879px;width:277px;height:419px;background:#fff;border-radius:30px;box-shadow:0 0 0 3px #f5f5f5,0 3px 10px rgba(0,0,0,.08);text-align:center}
.article .photo{position:absolute;left:8px;top:9px;width:261px;height:214px;border-radius:24px 24px 60px 60px}
.article h3{position:absolute;left:0;top:252px;width:100%;font:500 15px/23px var(--head);white-space:nowrap}
.article p{position:absolute;left:10px;top:306px;width:257px;font-size:11px;line-height:19px}
.article .more{left:71px;top:378px;width:135px;height:41px;border-radius:14px 14px 0 0;font:500 15px var(--head)}

/* footer */
.footer{position:absolute;left:0;top:3374px;width:1200px;height:376px;background:var(--footer);color:#fff}
.fcol{position:absolute;top:65px}
.fcol h4{font:500 17px var(--head);margin-bottom:18px;letter-spacing:.3px}
.fcol li{list-style:none;font-size:14px;line-height:28.6px}
.footer hr{position:absolute;left:172px;top:297px;width:856px;border:none;border-top:1px solid #bbb}
.copy{position:absolute;left:0;top:329px;width:100%;text-align:center;font-size:14px}
</style>
</head>
<body>

<header class="hero">
  <svg class="hero-arc" width="1200" height="808" viewBox="0 0 1200 808" aria-hidden="true">
    <circle cx="1290" cy="470" r="590" fill="#a8005e" opacity=".55"/>
    <circle cx="1290" cy="470" r="590" fill="none" stroke="#ef4fa3" stroke-width="10"/>
  </svg>
  <div class="hero-mark" role="img" aria-label="Faint line drawing of a fish made from joined dots"></div>
  <div class="hero-word">SEARCH</div>
  <div class="hero-person" role="img" aria-label="Smiling job seeker in a checked blazer with arms crossed"></div>
  <nav class="nav"><a>HOME</a><a>ABOUT</a><a>EMPLOYERS</a><a>SOLUTIONS</a><a>JOB SEEKERS</a><a>CONTACT</a></nav>
  <a class="post-job">POST A JOB</a>
  <h1 class="brand">KOROWAI STAFFING</h1>
  <p class="tagline">Find the right job for you</p>
  <form class="search">
    <div class="field" style="width:110px">Job Title</div>
    <div class="field" style="width:128px">All Locations <span class="caret"></span></div>
    <div class="field" style="width:144px">All Categories <span class="caret"></span></div>
    <div class="go">FIND JOBS</div>
  </form>
  <p class="search-note">Search your career opportunity through 12,800 jobs</p>
</header>

<section>
  <div class="sec-title" style="top:893px"><div class="ghost">HOW IT WORKS</div><h2>HOW IT WORKS</h2></div>
  <div class="step" style="left:170px">
    <div class="ico" style="background:var(--pink)">
      <svg width="66" height="74" viewBox="0 0 66 74" fill="none" stroke="#fff" stroke-width="2.5"><path d="M6 4h40v34M6 4v66h46l-6-6v-8"/><circle cx="18" cy="20" r="5"/><path d="M10 34c2-6 14-6 16 0M10 44h28M10 52h24M10 60h18M34 30l8 10 20-24"/></svg>
    </div>
    <div class="txt"><h3>REGISTER<br>YOUR ACCOUNT</h3><p>You need to create an account to find the best and preferred job.</p></div>
  </div>
  <div class="step" style="left:462px">
    <div class="ico" style="background:var(--plum-deep)">
      <svg width="80" height="80" viewBox="0 0 80 80" fill="none" stroke="#fff" stroke-width="2.5"><circle cx="34" cy="34" r="24"/><circle cx="34" cy="34" r="19"/><path d="M51 51l18 18M56 52l-4 4" stroke-width="5"/><text x="20" y="40" fill="#fff" stroke="none" font-family="Lexend,sans-serif" font-size="15">JOB</text></svg>
    </div>
    <div class="txt"><h3>APPLY<br>FOR DREAM JOB</h3><p>You need to create an account to find the best and preferred job.</p></div>
  </div>
  <div class="step" style="left:750px">
    <div class="ico" style="background:var(--rose)">
      <svg width="60" height="76" viewBox="0 0 60 76" fill="none" stroke="#fff" stroke-width="2.5"><path d="M4 4h36l16 16v52H4z"/><circle cx="30" cy="22" r="6"/><path d="M18 40c3-9 21-9 24 0M14 50h32M14 58h8l4 5 8-10M38 60h8"/></svg>
    </div>
    <div class="txt"><h3>UPLOAD<br>YOUR RESUME</h3><p>You need to create an account to find the best and preferred job.</p></div>
  </div>
</section>

<section>
  <div class="jobs-bg"></div>
  <div class="sec-title" style="top:1289px"><div class="ghost" style="font-size:40px;top:-20px;line-height:44px">FIND YOUR CAREER YOU<br>DESERVE IT</div><h2>FIND YOUR CAREER YOU DESERVE IT</h2></div>

  <article class="job" style="top:1369px">
    <div class="logo"><i></i>Lagoon Co</div>
    <h3>SENIOR WEB DESIGNER , DEVELOPER</h3>
    <p class="addr">48 Harbour Road, Suva, Fiji Islands</p>
    <div class="pay">$2500 / Month</div>
    <span class="tag" style="background:var(--green)">NEW</span>
    <a class="browse">BROWSE JOB</a>
  </article>
  <article class="job" style="top:1580px">
    <div class="logo"><i></i>Atoll Works</div>
    <h3>NEED SENIOR ROLLING STOCK TECHNICIAN</h3>
    <p class="addr">48 Harbour Road, Suva, Fiji Islands</p>
    <div class="pay">$2000 / Month</div>
    <span class="tag" style="background:var(--gold)">INTERSHIP</span>
    <a class="browse">BROWSE JOB</a>
  </article>
  <article class="job" style="top:1790px">
    <div class="logo"><i></i>Coral Freight</div>
    <h3>ART PRODUCTION SPECIALIST</h3>
    <p class="addr">48 Harbour Road, Suva, Fiji Islands</p>
    <div class="pay">$1200 / Month</div>
    <span class="tag" style="background:var(--teal)">FREELANCER</span>
    <a class="browse">BROWSE JOB</a>
  </article>
  <a class="btn" style="left:530px;top:2022px;width:138px;height:43px">Browse All Jobs</a>
</section>

<section>
  <div class="resume-person" role="img" aria-label="Young woman sitting cross-legged working on a laptop"></div>
  <div class="resume-panel">
    <p class="kicker">EXPLORE NEW LIFE</p>
    <h2>DON’T JUST FIND. BE FOUND<br>PUT YOUR CV IN FRONT OF<br>GREAT EMPLOYERS</h2>
    <p>Lorem Ipsum is simply dummy text of the printing and typesetting industry the standard dummy text ever since the when an printer took.</p>
    <a class="btn" style="left:42px;top:322px;width:210px;height:42px;gap:12px">Upload Your Resume
      <svg width="20" height="20" viewBox="0 0 20 20" fill="none" stroke="#fff" stroke-width="2"><path d="M10 14V2M5 7l5-5 5 5M2 12v6h16v-6"/></svg></a>
  </div>
</section>

<section>
  <div class="articles-bg"></div>
  <div class="sec-title" style="top:2793px"><div class="ghost">LATEST ARTICLE</div><h2>LATEST ARTICLE</h2></div>
  <article class="article" style="left:170px">
    <div class="photo" role="img" aria-label="Two colleagues reviewing a tablet together" style="background:linear-gradient(160deg,#e8e2dc,#8a8f98)"></div>
    <h3>JOB BOARD IS THE MOST<br>IMPORTANT</h3>
    <p>Lorem Ipsum is simply dummy text of the printing and typesetting industry the standard dummy text ever since the when an printer took.</p>
    <a class="btn more" style="background:var(--grey-btn)">READ MORE</a>
  </article>
  <article class="article" style="left:462px">
    <div class="photo" role="img" aria-label="Recruiter and candidate in an interview at a desk" style="background:linear-gradient(160deg,#dfe6ee,#5d6f88)"></div>
    <h3>HOW TO CONVINCE RECRUITERS<br>GET YOUR DREAM JOB</h3>
    <p>Lorem Ipsum is simply dummy text of the printing and typesetting industry the standard dummy text ever since the when an printer took.</p>
    <a class="btn more">READ MORE</a>
  </article>
  <article class="article" style="left:750px">
    <div class="photo" role="img" aria-label="Team of smiling coworkers in a bright office" style="background:linear-gradient(160deg,#eef0f2,#7d97b4)"></div>
    <h3>5 THINGS TO KNOW ABOUT<br>THE 2022 JOBS REPORT</h3>
    <p>Lorem Ipsum is simply dummy text of the printing and typesetting industry the standard dummy text ever since the when an printer took.</p>
    <a class="btn more" style="background:var(--grey-btn)">READ MORE</a>
  </article>
</section>

<footer class="footer">
  <div class="fcol" style="left:172px"><h4>FOR CANDIDATE</h4><ul><li>User Dashboard</li><li>Alert resume</li><li>Candidates</li><li>Blog List</li><li>Blog single</li></ul></div>
  <div class="fcol" style="left:389px"><h4>FOR EMPLOYERS</h4><ul><li>Post Jobs</li><li>Blog Grid</li><li>Contact</li><li>Jobs Listing</li><li>Jobs details</li></ul></div>
  <div class="fcol" style="left:629px"><h4>HELPFUL RESOURCES</h4><ul><li>FAQs</li><li>Employer detail</li><li>Profile</li><li>404 Page</li><li>Pricing</li></ul></div>
  <div class="fcol" style="left:914px"><h4>QUICK LINKS</h4><ul><li>Home</li><li>About us</li><li>Bookmark</li><li>Jobs</li><li>Employer</li></ul></div>
  <hr>
  <p class="copy">Copyright © 2022 All Rights Reserved.</p>
</footer>

</body>
</html>
```